Business Card Design for BrightlaneReach.com

--I need a business card design for my company BrightlaneReach.com

I have attached my logo...I want the brightlane reach logo on the front of the business card, and then I want The Brightlane Chief on the back of it with my information.

I would like to see a light colored background as well as a dark colored background

FRONT:
BRIGHTLANE REACH LOGO
247 E. Pelham Row
5th Floor
San Diego CA 92384
www.BrightlaneReach.com

Advanced Website & App Development
Websites, Apps, Online Voucher Systems

Leading Edge Marketing Services
SMS, VB, SMM, SEM,

BACK:
BRIGHTLANE CHIEF LOGO
Dorian Welker
The Brightlane Chief
Call Or Text: 555-204-3378
Dorian@BrightlaneChief.com
www.BrightlaneChief.com

Target Market(s)

small business owners

Industry/Entity Type

Business Consultant

Contact Information for Business Card

FRONT:
BRIGHTLANE REACH LOGO
247 E. Pelham Row
5th Floor
San Diego CA 92384
www.BrightlaneReach.com

SMS, VB, SMM, SEM,

BACK:
BRIGHTLANE CHIEF LOGO
Dorian Welker
The Brightlane Chief
Dorian@BrightlaneChief.com
www.BrightlaneChief.com

Requirements
Must have
• add this quote on it somewhere, anywhere,preferrably on back
• "The Fastest Way To Success Is To Take Action”
• — Dorian Welker, Brightlane Chief
Nice to have
• open
Should not have
• red

```html
<!DOCTYPE html>
<html lang="en">
<head>
<meta charset="utf-8">
<title>Brightlane Reach – Business Cards</title>
<link rel="stylesheet" href="https://fonts.googleapis.com/css2?family=Source+Sans+3:wght@400;600&display=swap">
<style>
  :root {
    --backdrop: #e4e6e8;
    --brand-blue: #0772ad;
    --card-white: #ffffff;
    --ink-grey: #6b6b6b;
    --rule-grey: #c9c9c9;
    --band-line: #b8bcc0;
  }
  html, body {
    margin: 0;
    width: 1105px;
    height: 1200px;
    overflow: hidden;
    background: var(--backdrop);
    font-family: "Source Sans 3", "Myriad Pro", sans-serif;
  }
  .card {
    position: absolute;
    left: 196px;
    width: 720px;
    height: 411px;
    box-sizing: border-box;
  }
  /* Front */
  .card--front {
    top: 146px;
    background: var(--brand-blue);
    color: var(--card-white);
  }
  .front-wordmark {
    position: absolute;
    left: 64px;
    top: 184px;
    width: 280px;
    text-align: center;
    font-size: 25px;
    font-weight: 400;
    letter-spacing: 2px;
    color: var(--card-white);
  }
  .front-details {
    position: absolute;
    left: 381px;
    top: 70px;
    font-size: 19px;
    line-height: 26px;
  }
  .front-details p { margin: 0; }
  .front-details .web { font-weight: 600; }
  .front-details .group { margin-top: 6px; }
  .front-details .group + .group { margin-top: 7px; }

  /* Back */
  .card--back {
    top: 602px;
    background: var(--card-white);
  }
  .back-wordmark {
    position: absolute;
    left: 73px;
    top: 196px;
    width: 281px;
    text-align: center;
    font-size: 25px;
    font-weight: 600;
    letter-spacing: 1.5px;
    color: var(--brand-blue);
  }
  .back-divider {
    position: absolute;
    left: 377px;
    top: 120px;
    width: 1px;
    height: 169px;
    background: var(--rule-grey);
  }
  .person {
    position: absolute;
    left: 398px;
    top: 122px;
  }
  .person-name {
    margin: 0;
    font-size: 27px;
    font-weight: 600;
    color: var(--brand-blue);
    line-height: 32px;
  }
  .person-title {
    margin: 0 0 14px;
    font-size: 20px;
    color: var(--ink-grey);
    line-height: 26px;
  }
  .contact-list { list-style: none; margin: 0; padding: 0; }
  .contact-list li {
    display: flex;
    align-items: center;
    gap: 10px;
    font-size: 19px;
    line-height: 27.5px;
    color: var(--ink-grey);
  }
  .contact-list svg { width: 16px; height: 16px; fill: var(--brand-blue); flex: none; }
  .back-band-line {
    position: absolute;
    left: 0; right: 0;
    top: 379px;
    height: 3px;
    background: var(--band-line);
  }
  .back-band {
    position: absolute;
    left: 0; right: 0;
    top: 385px;
    bottom: 0;
    background: var(--brand-blue);
    display: flex;
    align-items: center;
    justify-content: center;
  }
  .quote {
    margin: 0;
    font-size: 13px;
    line-height: 16px;
    letter-spacing: 0.3px;
    color: var(--card-white);
    white-space: nowrap;
  }
</style>
</head>
<body>

<section class="card card--front" aria-label="Card front">
  <div class="front-wordmark">BRIGHTLANE REACH</div>
  <div class="front-details">
    <p>247 E. Pelham Row</p>
    <p>5th Floor</p>
    <p>San Diego CA 92384</p>
    <p class="web">BrightlaneReach.com</p>
    <div class="group">
      <p>Advanced Website &amp;</p>
      <p>App Development</p>
      <p>Websites • Apps</p>
      <p>Online Voucher Systems</p>
    </div>
    <div class="group">
      <p>Leading Edge Marketing Services</p>
      <p>SMS • VB • SMM • SEM</p>
    </div>
  </div>
</section>

<section class="card card--back" aria-label="Card back">
  <div class="back-wordmark">BRIGHTLANE CHIEF</div>
  <div class="back-divider"></div>
  <div class="person">
    <p class="person-name">Dorian Welker</p>
    <p class="person-title">The Brightlane Chief</p>
    <ul class="contact-list">
      <li>
        <svg viewBox="0 0 16 16" aria-hidden="true"><path d="M3.6 1.2l2.2 2.6c.3.4.3.9 0 1.3L4.7 6.3c.9 2 2.9 4 5 5l1.2-1.1c.4-.3.9-.3 1.3 0l2.6 2.2c.4.3.4.9.1 1.3l-1.1 1.2c-.5.5-1.2.7-1.9.5C6.9 14 2 9.1.6 4.1.4 3.4.6 2.7 1.1 2.2L2.3 1.1c.4-.3 1-.3 1.3.1z"/></svg>
        555-204-3378
      </li>
      <li>
        <svg viewBox="0 0 16 16" aria-hidden="true"><path d="M1 3h14v1.2L8 9.2 1 4.2z"/><path d="M1 5.6l7 5 7-5V13H1z"/></svg>
        Dorian@BrightlaneChief.com
      </li>
      <li>
        <svg viewBox="0 0 16 16" aria-hidden="true"><circle cx="8" cy="8" r="7.5"/><path d="M8 .8v14.4M.8 8h14.4M8 .8c-4 3.6-4 10.8 0 14.4M8 .8c4 3.6 4 10.8 0 14.4" fill="none" stroke="#ffffff" stroke-width="1"/></svg>
        www.BrightlaneChief.com
      </li>
    </ul>
  </div>
  <div class="back-band-line"></div>
  <div class="back-band">
    <p class="quote">“The Fastest Way To Success Is To Take Action” — Dorian Welker, Brightlane Chief</p>
  </div>
</section>

</body>
</html>
```